"Trade with Tilda" needs a funky and stylish business card

Hi my name is Tilda, I am an experienced Bidnest Prime Vendor with a 100% satisfaction rating and over 400 items sold

My business name and bidnest username is "Trade with Tilda" I sell other peoples items on Bidnest for a commission. The main items I sell are furniture and renovation/building salvage items such as used kitchens, bathrooms , window doors etc.

I will be promoting my service in real estate agent offices, storage facilities, removalists, building and renovating companies.

i believe selling on bidnest is a great way for people to recycle their used goods and salvageable materials and reduce waste and landfill.

Target Market(s)

people selling their homes, renovators, builders, downsizers

Industry/Entity Type

Real Estate

Contact Information for Business Card

Tilda Marlowe
0492716045

Logo Text

Trade with Tilda

Logo styles of interest
Wordmark Logo
Requirements
Must have
• the business card must feature the bidnest logo mentioning primevendorr gold ranked vendor I have attached a copy
Nice to have
• i would like to have the trade with tilda logo written in royal blue

```html
<!DOCTYPE html>
<html lang="en">
<head>
<meta charset="utf-8">
<title>Trade with Tilda – Business Card</title>
<link rel="stylesheet" href="https://fonts.googleapis.com/css2?family=Gelasio:wght@400&display=swap">
<style>
  :root {
    --royal-blue: #1530f0;
    --card-blue: #4569ff;
    --paper: #ffffff;
    --badge-gold: #f3b72b;
    --badge-rim: #d99a1c;
  }
  html, body {
    margin: 0;
    padding: 0;
    width: 1200px;
    height: 694px;
    overflow: hidden;
    background: var(--paper);
  }
  .card {
    position: relative;
    width: 1200px;
    height: 694px;
    overflow: hidden;
    background: var(--paper);
    font-family: "Gelasio", Georgia, serif;
  }
  .card__bands {
    position: absolute;
    inset: 0;
    width: 1200px;
    height: 694px;
  }
  .contact {
    position: absolute;
    left: 79px;
    top: 104px;
    color: var(--royal-blue);
  }
  .contact__name {
    margin: 0;
    font-size: 48px;
    font-weight: 400;
    line-height: 1;
    letter-spacing: 1px;
  }
  .contact__phone {
    margin: 26px 0 0;
    font-size: 46px;
    font-weight: 400;
    line-height: 1;
    letter-spacing: 1px;
    font-variant-numeric: oldstyle-nums;
  }
  .business-name {
    position: absolute;
    left: 641px;
    top: 312px;
    margin: 0;
    color: var(--paper);
    font-size: 35px;
    font-weight: 400;
    line-height: 1;
    letter-spacing: 3px;
    text-transform: uppercase;
    white-space: nowrap;
  }
  .vendor-badge {
    position: absolute;
    left: 773px;
    top: 467px;
    width: 115px;
    height: 115px;
    border-radius: 50%;
    background: var(--badge-gold);
    box-shadow: inset 0 0 0 5px var(--badge-rim);
  }
  .marketplace-mark {
    position: absolute;
    right: 68px;
    top: 568px;
    color: var(--paper);
    font-weight: 400;
    text-align: right;
  }
  .marketplace-mark__name {
    margin: 0;
    font-size: 56px;
    font-weight: 400;
    line-height: 1;
  }
  .marketplace-mark__tier {
    margin: 6px 0 0;
    font-size: 22px;
    font-weight: 400;
    line-height: 1;
  }
</style>
</head>
<body>
  <main class="card">
    <svg class="card__bands" viewBox="0 0 1061 614" preserveAspectRatio="none" aria-hidden="true">
      <rect class="top-rule" x="0" y="0" width="1061" height="3" fill="var(--royal-blue)"/>
      <polygon class="lower-panel" points="0,300 506,300 506,264 1061,264 1061,614 0,614" fill="var(--card-blue)"/>
      <path class="step-band-lower" d="M0 295 H549 Q556 295 556 300.5 Q556 306 549 306 H0 Z" fill="var(--royal-blue)"/>
      <rect class="step-band-stem" x="500" y="258" width="12" height="43" rx="4" fill="var(--royal-blue)"/>
      <rect class="step-band-upper" x="500" y="258" width="561" height="12" rx="4" fill="var(--royal-blue)"/>
    </svg>

    <section class="contact">
      <h1 class="contact__name">Tilda Marlowe</h1>
      <p class="contact__phone">0492716045</p>
    </section>

    <p class="business-name">Trade with Tilda</p>

    <div class="vendor-badge" role="img" aria-label="Gold ranked vendor badge"></div>

    <div class="marketplace-mark">
      <p class="marketplace-mark__name">Bidnest</p>
      <p class="marketplace-mark__tier">Prime Vendor</p>
    </div>
  </main>
</body>
</html>
```